Logo and Card design for KLV Home Solutions LLC

I need an edgier logo and business card designs. Current logo attached. I like the colors below. I would like the logo to incorporate a home in the design.
Title = Principal-Acquisitions
Email:KLVHOMESOLUTIONS@maplenest-mail.com
412-907-2153
facebook
IG
2 sided business card with the front being contact info a slogan about selling a home fast. The back incorporating What we do. Buy houses, land, or commercial property as is. We find solutions to make the process of selling simple and fair.

Target Market(s)

Motivated house sellers.

Industry/Entity Type

Business

Contact Information for Business Card

Who we are: We are a Faith based Real Estate Investment Company. We pay cash for homes in any condition and can close quick. Whatever the reason you need to sell fast, we can help. We believe in creating win-win solutions to help you in your time of need. We care! We can help!

Logo Text

KLV Home Solutions LLC

Font styles to use
Sans Serif

Colors
33a6d7
0355a3
85abd2
cee9f5
9d9d9d
b2b2b2
ffffff

Requirements
Must have
• Old logo attached. I want something edgier.
• Company name, phone number, description on the back of what we can do. Pay all cash. Buy in as is condition. No fees,Commisions or closing costs.Close quick. No hassles with solutions to meet your unique situation.
• Call today for an offer within 24 hours.

```html
<!DOCTYPE html>
<html lang="en">
<head>
<meta charset="utf-8">
<title>KLV Home Solutions – Business Card</title>
<link rel="stylesheet" href="https://fonts.googleapis.com/css2?family=Work+Sans:wght@400;500;600;700&display=swap">
<style>
  :root {
    --navy: #243a73;
    --gray-dark: #6f6f6f;
    --gray-light: #9d9d9d;
    --white: #ffffff;
    --backdrop: #e4e4e4;
  }
  * { margin: 0; padding: 0; box-sizing: border-box; }
  html, body { width: 1200px; height: 1130px; overflow: hidden; }
  body {
    background: var(--backdrop);
    font-family: "Work Sans", sans-serif;
    position: relative;
  }
  .card {
    position: absolute;
    left: 170px;
    width: 860px;
    height: 490px;
    overflow: hidden;
    box-shadow: 0 4px 10px rgba(0,0,0,.22);
  }
  .card--front { top: 60px; background: var(--white); }
  .card--back { top: 600px; background: var(--navy); }

  .card__waves { position: absolute; inset: 0; }

  .wordmark {
    position: absolute;
    font-weight: 600;
    line-height: 1;
    white-space: nowrap;
  }
  .card--front .wordmark {
    left: 30px;
    top: 118px;
    font-size: 26px;
    color: var(--navy);
  }
  .card--back .wordmark {
    left: 0;
    right: 0;
    top: 190px;
    text-align: center;
    font-size: 38px;
    color: var(--white);
  }

  .title-block {
    position: absolute;
    right: 32px;
    top: 112px;
    text-align: right;
    color: var(--navy);
  }
  .title-block__company { font-size: 34px; font-weight: 600; line-height: 1; }
  .title-block__role { font-size: 19px; margin-top: 6px; }
  .title-bar {
    position: absolute;
    right: 0;
    top: 112px;
    width: 10px;
    height: 58px;
    background: var(--navy);
  }

  .contacts {
    position: absolute;
    right: 30px;
    top: 280px;
    list-style: none;
    color: var(--white);
    font-size: 20px;
    line-height: 26px;
    text-align: right;
  }
  .contacts li { display: flex; justify-content: flex-end; align-items: center; gap: 12px; }
  .contacts__dot {
    width: 14px; height: 14px; border-radius: 50%;
    background: var(--white); display: inline-block;
  }
  .slogan {
    position: absolute;
    right: 30px;
    top: 428px;
    color: var(--white);
    font-size: 19px;
    font-weight: 600;
    letter-spacing: 3px;
  }

  .offer {
    position: absolute;
    left: 0; right: 0;
    top: 352px;
    color: var(--white);
    font-size: 20px;
    line-height: 27px;
    text-align: center;
  }
</style>
</head>
<body>
  <section class="card card--front">
    <svg class="card__waves" width="860" height="490" viewBox="0 0 860 490">
      <path d="M0 490 C170 300 470 215 860 200 L860 490 Z" fill="var(--gray-light)"/>
      <path d="M0 490 C190 310 490 225 860 212 L860 490 Z" fill="var(--gray-dark)"/>
      <path d="M30 490 C220 320 520 232 860 222 L860 490 Z" fill="var(--navy)"/>
    </svg>
    <div class="wordmark">KLV Home Solutions</div>
    <div class="title-block">
      <div class="title-block__company">KLV HOME SOLUTIONS</div>
      <div class="title-block__role">Principal-Acquisitions</div>
    </div>
    <div class="title-bar"></div>
    <ul class="contacts">
      <li>412-907-2153 <span class="contacts__dot"></span></li>
      <li>/klvhomesolutions <span class="contacts__dot"></span></li>
      <li>@klvhomesolutions <span class="contacts__dot"></span></li>
      <li>KLVHOMESOLUTIONS@maplenest-mail.com <span class="contacts__dot"></span></li>
    </ul>
    <div class="slogan">SELLING A HOME FAST</div>
  </section>

  <section class="card card--back">
    <div class="wordmark">KLV Home Solutions</div>
    <p class="offer">
      Pay all cash. Buy in as is condition. No fees,Commisions<br>
      or closing costs.Close quick. No hassles with solutions<br>
      to meet your unique situation.<br>
      Call today for an offer within 24 hours.
    </p>
  </section>
</body>
</html>
```